hello! I need a very simple modern business card for a new venture called The Quiet Harbour Asia. It's the very first Tech-Free retreat in Asia!

The concept is very unique. Basically a group of 12-15 people would go on a 3 to 4 days retreat where no phone or internet is allowed. The first retreat will take place in a beautiful villa in Bali by the sea. It will include yoga, meditation, art & writing workshops, swimming, hiking, cooking, healthy vegetarian meals, etc.

Reason: Thanks for your submissions. I still haven't found exactly what I'm after but the designs that haven't be eliminated are getting close.. Please keep in mind that it should be a simple, modern and upmarket business card. Thanks

Target Market(s)

Both men and women who would like to disconnect from life, computer and phone for 3/4 days. They can be either local or expats but based in Asia (Singapore, Hong Kong).
Client will have to pay for their own flight and then the price is around US$600 for a 3-day retreat including everything (accommodation, food, activities). It means clients already have a good income. They are usually working in marketing, advertising, digital media, public relations.

Industry/Entity Type

Internet

Font styles to use
Other font styles liked:
• anything modern you like

Colors
acd036
9bcb3c
f37022
f68d4d
1b1b1b
333333
acd037

Requirements
Must have
• Name: Rel Vontaine
Position: #screenwanderer
Company: The Quiet Harbour Asia (asia should be smaller than the rest)
- Email button - quietharbourasia@mailnest.example
- Facepage button - www.facepage.example/quietharbourasia
- Ticketloom button - www.quietharbourasia.ticketloom.example
Nice to have
• You can use my logo attached but it's something I designed quickly on Power Point so it would be nice to include your own version.
Should not have
• anything tacky or girly or childish. thanks

```html
<!DOCTYPE html>
<html lang="en">
<head>
<meta charset="utf-8">
<title>The Quiet Harbour Asia — Business Card</title>
<link rel="stylesheet" href="https://fonts.googleapis.com/css2?family=Didact+Gothic&display=swap">
<style>
  :root {
    --lime: #acd036;
    --green: #9bcb3c;
    --orange: #f37022;
    --orange-soft: #f68d4d;
    --ink: #1b1b1b;
    --charcoal: #333333;
    --lime-alt: #acd037;
    --paper: #ffffff;
  }
  * { margin: 0; padding: 0; box-sizing: border-box; }
  html, body { width: 1200px; height: 1050px; overflow: hidden; background: var(--paper); }
  body { font-family: "Didact Gothic", "Century Gothic", sans-serif; position: relative; }

  .card { position: absolute; width: 510px; height: 310px; overflow: hidden; }
  .card--green { background: var(--green); }
  .card--orange { background: var(--orange); }
  .card__shapes { position: absolute; inset: 0; width: 100%; height: 100%; }

  .front-green { left: 60px; top: 30px; }
  .back-green { left: 642px; top: 30px; }
  .front-orange { left: 60px; top: 355px; }
  .back-orange { left: 642px; top: 355px; }

  .brand { position: absolute; display: flex; align-items: center; gap: 14px; color: var(--charcoal); }
  .brand__dot { width: 66px; height: 66px; border-radius: 50%; background: var(--orange); flex: none; }
  .card--orange .brand__dot { background: var(--orange-soft); }
  .brand__name { line-height: 1; }
  .brand__the { display: block; font-size: 25px; }
  .brand__main { display: block; font-size: 28px; margin-top: 2px; }
  .brand__region { display: block; font-size: 16px; margin-top: 1px; }

  .front-green .brand, .front-orange .brand { left: 33px; top: 33px; }
  .back-green .brand, .back-orange .brand { left: 96px; top: 112px; }
  .back-green .brand__dot, .back-orange .brand__dot { width: 72px; height: 72px; }

  .person { position: absolute; left: 33px; top: 138px; }
  .person__name { font-size: 32px; line-height: 1; }
  .person__role { font-size: 19px; margin-top: 6px; margin-left: 4px; }
  .front-green .person { color: var(--lime); }
  .front-orange .person { color: var(--charcoal); }

  .contacts { position: absolute; left: 28px; top: 218px; list-style: none; }
  .contacts li { display: flex; align-items: center; gap: 7px; height: 24px; font-size: 14px; }
  .front-green .contacts li { color: var(--lime); }
  .front-orange .contacts li { color: var(--paper); }
  .contacts__mark { width: 16px; height: 16px; border-radius: 50%; background: var(--lime); flex: none; }
  .front-orange .contacts__mark { background: var(--lime-alt); }
  .contacts__icon { width: 16px; height: 16px; flex: none; }

  .back-shadow { position: absolute; left: 180px; top: 232px; width: 150px; height: 24px; border-radius: 50%; filter: blur(8px); }
  .back-green .back-shadow { background: rgba(60, 90, 20, 0.45); }
  .back-orange .back-shadow { background: rgba(120, 40, 0, 0.45); }

  .palette { position: absolute; left: 629px; top: 692px; display: flex; gap: 19px; list-style: none; }
  .palette li { width: 56px; height: 56px; border-radius: 50%; }
  .swatch-lime { background: var(--lime); }
  .swatch-green { background: var(--green); }
  .swatch-orange { background: var(--orange); }
  .swatch-orange-soft { background: var(--orange-soft); }
  .swatch-ink { background: var(--ink); }
  .swatch-charcoal { background: var(--charcoal); }
  .swatch-lime-alt { background: var(--lime-alt); }
</style>
</head>
<body>

  <!-- Green front -->
  <section class="card card--green front-green">
    <svg class="card__shapes" viewBox="0 0 510 310" aria-hidden="true">
      <path d="M0 160 Q0 118 45 118 L300 118 Q480 128 510 300 L510 310 L0 310 Z" fill="var(--charcoal)"/>
      <path d="M385 10 L498 10 L498 88 Q470 28 385 10 Z" fill="var(--charcoal)"/>
    </svg>
    <div class="brand">
      <span class="brand__dot"></span>
      <div class="brand__name">
        <span class="brand__the">The</span>
        <span class="brand__main">Quiet Harbour</span>
        <span class="brand__region">Asia</span>
      </div>
    </div>
    <div class="person">
      <div class="person__name">Rel Vontaine</div>
      <div class="person__role">#screenwanderer</div>
    </div>
    <ul class="contacts">
      <li>
        <svg class="contacts__icon" viewBox="0 0 16 16" aria-hidden="true"><circle cx="8" cy="8" r="8" fill="var(--lime)"/><rect x="3.5" y="5" width="9" height="6" fill="var(--charcoal)"/><path d="M3.5 5 L8 8.5 L12.5 5" fill="none" stroke="var(--lime)" stroke-width="1"/></svg>
        quietharbourasia@mailnest.example
      </li>
      <li><span class="contacts__mark"></span>www.facepage.example/quietharbourasia</li>
      <li><span class="contacts__mark"></span>www.quietharbourasia.ticketloom.example</li>
    </ul>
  </section>

  <!-- Green back -->
  <section class="card card--green back-green">
    <div class="back-shadow"></div>
    <div class="brand">
      <span class="brand__dot"></span>
      <div class="brand__name">
        <span class="brand__the">The</span>
        <span class="brand__main">Quiet Harbour</span>
        <span class="brand__region">Asia</span>
      </div>
    </div>
  </section>

  <!-- Orange front -->
  <section class="card card--orange front-orange">
    <svg class="card__shapes" viewBox="0 0 510 310" aria-hidden="true">
      <path d="M0 165 Q0 125 45 125 L300 125 Q480 135 510 300 L510 310 L0 310 Z" fill="var(--orange-soft)"/>
      <path d="M385 10 L498 10 L498 88 Q470 28 385 10 Z" fill="var(--orange-soft)"/>
    </svg>
    <div class="brand">
      <span class="brand__dot"></span>
      <div class="brand__name">
        <span class="brand__the">The</span>
        <span class="brand__main">Quiet Harbour</span>
        <span class="brand__region">Asia</span>
      </div>
    </div>
    <div class="person">
      <div class="person__name">Rel Vontaine</div>
      <div class="person__role">#screenwanderer</div>
    </div>
    <ul class="contacts">
      <li>
        <svg class="contacts__icon" viewBox="0 0 16 16" aria-hidden="true"><circle cx="8" cy="8" r="8" fill="var(--lime-alt)"/><rect x="3.5" y="5" width="9" height="6" fill="var(--charcoal)"/><path d="M3.5 5 L8 8.5 L12.5 5" fill="none" stroke="var(--lime-alt)" stroke-width="1"/></svg>
        quietharbourasia@mailnest.example
      </li>
      <li><span class="contacts__mark"></span>www.facepage.example/quietharbourasia</li>
      <li><span class="contacts__mark"></span>www.quietharbourasia.ticketloom.example</li>
    </ul>
  </section>

  <!-- Orange back -->
  <section class="card card--orange back-orange">
    <div class="back-shadow"></div>
    <div class="brand">
      <span class="brand__dot"></span>
      <div class="brand__name">
        <span class="brand__the">The</span>
        <span class="brand__main">Quiet Harbour</span>
        <span class="brand__region">Asia</span>
      </div>
    </div>
  </section>

  <!-- Colour palette -->
  <ul class="palette" aria-label="Colour palette">
    <li class="swatch-lime"></li>
    <li class="swatch-green"></li>
    <li class="swatch-orange"></li>
    <li class="swatch-orange-soft"></li>
    <li class="swatch-ink"></li>
    <li class="swatch-charcoal"></li>
    <li class="swatch-lime-alt"></li>
  </ul>

</body>
</html>
```